Makeup Artist

Hi I am makeup artist I attached the business card that I found on the net love the design.
I would love something like this simple but looking expensive.
I want double side business card. Front my full name. my phone number, email address and facebook and my next appointment is... on the other side.
Thank you :)

Hello I change my Facebook account - Makeup by Liora, if you could please update your designs , thank you

Target Market(s)

high end clientele

Industry/Entity Type

Business

Colors
ec2027
ffc214
33b7a4
6b449b
e34197
9bcb3c
f37122
a64599

Requirements
Must have
• bright colours
Should not have
• brushes or whole lipsticks

```html
<!DOCTYPE html>
<html lang="en">
<head>
<meta charset="utf-8">
<title>Liora Vesnik – Business Card</title>
<link rel="stylesheet" href="https://fonts.googleapis.com/css2?family=Playfair+Display:wght@400&family=Yellowtail&display=swap">
<style>
  :root {
    --stage: #e9e7e5;
    --card-white: #ffffff;
    --card-edge: #d9d9db;
    --ink: #1c1a1a;
    --accent-red: #c4122a;
    --swatch-red: #d5131f;
    --swatch-rose: #c9566c;
    --swatch-nude: #a87a72;
  }
  * { box-sizing: border-box; margin: 0; padding: 0; }
  html, body {
    width: 1200px; height: 873px; overflow: hidden;
    background: var(--stage);
  }
  .canvas { position: relative; width: 1200px; height: 873px; }
  .card {
    position: absolute; top: 278px;
    width: 520px; height: 316px;
    border-radius: 3px;
    box-shadow: 0 6px 18px rgba(0,0,0,0.12);
    overflow: hidden;
  }
  .card--front {
    left: 60px;
    background: radial-gradient(ellipse at 58% 55%, #ffffff 30%, #f0f0f1 70%, var(--card-edge) 100%);
  }
  .card--back { left: 620px; background: var(--card-white); }
  .swatches {
    position: absolute; left: 150px; top: 26px;
    width: 84px; height: 48px;
    border-radius: 20px 28px 22px 16px;
    background: linear-gradient(100deg, var(--swatch-nude) 0%, var(--swatch-rose) 45%, var(--swatch-red) 80%);
  }
  .brand-name {
    position: absolute; left: 40px; right: 40px; top: 80px;
    text-align: center;
    font-family: "Yellowtail", cursive;
    font-weight: 400;
    font-size: 54px; line-height: 1.1;
    color: var(--accent-red);
    white-space: nowrap;
  }
  .contacts {
    position: absolute; left: 60px; top: 174px;
    list-style: none;
    font-family: "Playfair Display", serif;
    font-size: 21px; color: var(--ink);
  }
  .contacts li {
    display: flex; align-items: center; gap: 12px;
    height: 38px;
  }
  .icon { width: 18px; height: 18px; flex: none; }
  .social-square {
    width: 18px; height: 18px; flex: none;
    background: var(--accent-red);
  }
  .appointment {
    position: absolute; left: 34px; top: 30px;
    font-family: "Playfair Display", serif;
    font-size: 20px; color: var(--ink);
  }
</style>
</head>
<body>
<main class="canvas">
  <section class="card card--front" aria-label="Front of business card">
    <div class="swatches" role="img" aria-label="Lipstick colour swatches in nude, rose and red"></div>
    <h1 class="brand-name">Liora Vesnik</h1>
    <ul class="contacts">
      <li class="phone">
        <svg class="icon" viewBox="0 0 24 24" aria-hidden="true"><path d="M6.6 10.8a15 15 0 0 0 6.6 6.6l2.2-2.2c.3-.3.7-.4 1-.2 1.1.4 2.3.6 3.6.6.6 0 1 .4 1 1V20c0 .6-.4 1-1 1A17 17 0 0 1 3 4c0-.6.4-1 1-1h3.5c.6 0 1 .4 1 1 0 1.3.2 2.5.6 3.6.1.3 0 .7-.2 1z" fill="#c4122a"/></svg>
        <span>0400 555 318</span>
      </li>
      <li class="email">
        <svg class="icon" viewBox="0 0 24 24" aria-hidden="true"><rect x="2" y="5" width="20" height="14" fill="none" stroke="#c4122a" stroke-width="2"/><path d="M2 5l10 8 10-8M2 19l7-7M22 19l-7-7" fill="none" stroke="#c4122a" stroke-width="1.6"/></svg>
        <span>lioravesnik@mailbox.com</span>
      </li>
      <li class="social">
        <span class="social-square" aria-hidden="true"></span>
        <span>Makeup by Liora</span>
      </li>
    </ul>
  </section>

  <section class="card card--back" aria-label="Back of business card">
    <p class="appointment">My next appointment is...</p>
  </section>
</main>
</body>
</html>
```